Health and Wellness company needs flyer to promote free seminar

Stride reform studio is a health and wellness company that offers an exercise program designed by physical therapists to help relieve pain and improve mobility. Our business is a new concept that is not well understood by the public. In order to promote our business we offer a free seminar where we present information regarding the underlying cause of pain and tightness. During the seminar we also perform a posture screen and movement testing for all participants.

Target Market(s)

Mostly healthy and active women ages 25-65

Industry/Entity Type

Health And Wellness

Font styles to use
Sans Serif

Colors

Designer to choose colors to be used in the design.

Requirements
Must have
• Title: Eliminate Pain and Tightness For Good
• Paragraph: Stride Reform Studio offers a free 60 minute seminar: "The Busy Walker's Handbook to Bending and Standing Taller."
• What to Expect:
• • Identify the underlying cause of your pain and mobility issues
• • Expose what gets in the way of you moving and feeling better
• • Learn why traditional exercises don’t help and can actually make the problem worse
• • Reveal what your posture is saying and how that impacts you
• • Experience your muscle imbalances through movement tests
• • Discover the training method that realigns your posture, increases your mobility and reduces your pain
• Call to action: RSVP online at stridereformstudio.com
Nice to have
• Use a relevant image showing a female dealing with tightness in the low back, legs, etc.
• Emphasize that the seminar is FREE.
• Make the call to action prominent.

```html
<!DOCTYPE html>
<html lang="en">
<head>
<meta charset="utf-8">
<title>Stride Reform Studio – Free Seminar</title>
<link rel="stylesheet" href="https://fonts.googleapis.com/css2?family=Open+Sans:wght@400;700&family=Roboto+Condensed:wght@700&display=swap">
<style>
  :root {
    --purple: #5a5bb0;
    --orange: #f7941d;
    --ink: #222222;
    --white: #ffffff;
    --backdrop: #d9d9d9;
    --band-light: #f4f4f4;
    --band-mid: #cfcfcf;
  }
  html, body {
    margin: 0;
    width: 1020px;
    height: 1200px;
    overflow: hidden;
    background: var(--backdrop);
  }
  .flyer {
    position: absolute;
    left: 93px;
    top: 10px;
    width: 834px;
    height: 1180px;
    background: var(--white);
    overflow: hidden;
    font-family: "Open Sans", Arial, sans-serif;
    color: var(--ink);
  }
  .hero-photo {
    position: absolute;
    left: 0; top: 104px;
    width: 834px; height: 469px;
    background: linear-gradient(120deg, #3a4350 0%, #8d96a3 35%, #c7ced8 55%, #6f87b4 72%, #3b4250 100%);
  }
  .header-shapes {
    position: absolute;
    left: 0; top: 0;
  }
  .brand {
    position: absolute;
    left: 20px; top: 46px;
    display: flex;
    align-items: center;
    gap: 12px;
  }
  .brand-mark {
    width: 26px; height: 26px;
    background: var(--orange);
  }
  .brand-name {
    font-size: 22px;
    font-weight: 700;
    color: var(--purple);
    white-space: nowrap;
  }
  .free-seminar {
    position: absolute;
    right: 26px; top: 14px;
    margin: 0;
    font-family: "Roboto Condensed", "Arial Narrow", sans-serif;
    font-weight: 700;
    font-size: 66px;
    line-height: 76px;
    letter-spacing: 1px;
    background: linear-gradient(180deg, #ffffff 0%, #e6e6e6 45%, #a9a9a9 55%, #f2f2f2 100%);
    -webkit-background-clip: text;
    background-clip: text;
    color: transparent;
  }
  .title-band {
    position: absolute;
    left: 0; top: 573px;
    width: 834px; height: 127px;
    background: linear-gradient(90deg, var(--band-mid) 0%, var(--band-light) 35%, var(--band-light) 65%, var(--band-mid) 100%);
    text-align: center;
  }
  .headline {
    margin: 26px 0 0;
    font-family: "Roboto Condensed", "Arial Narrow", sans-serif;
    font-weight: 700;
    font-size: 42px;
    line-height: 46px;
    color: var(--purple);
    letter-spacing: 0.3px;
  }
  .subhead {
    margin: 4px 0 0;
    font-weight: 700;
    font-size: 18.5px;
    text-transform: uppercase;
    color: var(--ink);
  }
  .expect-tab {
    position: absolute;
    left: 0; top: 720px;
  }
  .expect-title {
    position: absolute;
    left: 52px; top: 724px;
    margin: 0;
    font-family: "Roboto Condensed", "Arial Narrow", sans-serif;
    font-weight: 700;
    font-size: 42px;
    line-height: 56px;
    color: var(--white);
  }
  .expect-list {
    position: absolute;
    left: 28px; top: 798px;
    width: 760px;
    margin: 0; padding: 0;
    list-style: none;
    font-size: 17.5px;
    line-height: 24px;
  }
  .expect-list li {
    position: relative;
    padding-left: 28px;
    margin-bottom: 15px;
  }
  .expect-list svg {
    position: absolute;
    left: 0; top: 6px;
  }
  .expect-list strong { font-weight: 700; }
  .footer-waves {
    position: absolute;
    left: 0; top: 999px;
  }
  .cta {
    position: absolute;
    left: 0; top: 1116px;
    width: 834px;
    margin: 0;
    text-align: center;
    font-weight: 700;
    font-size: 29px;
    color: var(--white);
  }
</style>
</head>
<body>
<main class="flyer">
  <div class="hero-photo" role="img" aria-label="Photo of a woman in a blue sports top squatting with a barbell on her shoulders in a gym"></div>

  <svg class="header-shapes" width="834" height="130" viewBox="0 0 834 130" aria-hidden="true">
    <polygon points="0,0 312,0 347,127 0,127" fill="var(--white)"/>
    <polygon points="312,0 834,0 834,104 341,104" fill="var(--purple)"/>
  </svg>

  <div class="brand">
    <span class="brand-mark"></span>
    <span class="brand-name">Stride Reform Studio</span>
  </div>
  <h1 class="free-seminar">FREE SEMINAR</h1>

  <section class="title-band">
    <h2 class="headline">ELIMINATE PAIN AND TIGHTNESS FOR GOOD</h2>
    <p class="subhead">The Busy Walker's Handbook to Bending and Standing Taller</p>
  </section>

  <svg class="expect-tab" width="480" height="64" viewBox="0 0 480 64" aria-hidden="true">
    <polygon points="0,0 396,0 370,64 0,64" fill="var(--purple)"/>
    <polygon points="410,0 432,0 406,64 384,64" fill="var(--orange)"/>
    <polygon points="440,0 462,0 436,64 414,64" fill="var(--orange)"/>
    <polygon points="470,0 480,0 480,3 466,64 444,64" fill="var(--orange)"/>
  </svg>
  <h3 class="expect-title">What to Expect</h3>

  <ul class="expect-list">
    <li><svg width="14" height="12" viewBox="0 0 14 12"><path d="M1 6 L5 10 L13 1" fill="none" stroke="var(--orange)" stroke-width="2"/></svg><strong>Identify</strong> the underlying cause of your pain and mobility issues</li>
    <li><svg width="14" height="12" viewBox="0 0 14 12"><path d="M1 6 L5 10 L13 1" fill="none" stroke="var(--orange)" stroke-width="2"/></svg><strong>Expose</strong> what gets in the way of you moving and feeling better</li>
    <li><svg width="14" height="12" viewBox="0 0 14 12"><path d="M1 6 L5 10 L13 1" fill="none" stroke="var(--orange)" stroke-width="2"/></svg><strong>Learn</strong> why traditional exercises don’t help and can actually make the problem worse</li>
    <li><svg width="14" height="12" viewBox="0 0 14 12"><path d="M1 6 L5 10 L13 1" fill="none" stroke="var(--orange)" stroke-width="2"/></svg><strong>Reveal</strong> what your posture is saying and how that impacts you</li>
    <li><svg width="14" height="12" viewBox="0 0 14 12"><path d="M1 6 L5 10 L13 1" fill="none" stroke="var(--orange)" stroke-width="2"/></svg><strong>Experience</strong> your muscle imbalances through movement tests</li>
    <li><svg width="14" height="12" viewBox="0 0 14 12"><path d="M1 6 L5 10 L13 1" fill="none" stroke="var(--orange)" stroke-width="2"/></svg><strong>Discover</strong> the training method that realigns your posture, increases your mobility and reduces your pain</li>
  </ul>

  <svg class="footer-waves" width="834" height="181" viewBox="0 0 834 181" aria-hidden="true">
    <path d="M0,128 Q400,-10 834,118 L834,181 L0,181 Z" fill="var(--purple)"/>
    <path d="M0,136 Q400,2 834,128 L834,181 L0,181 Z" fill="var(--white)"/>
    <path d="M0,142 Q400,10 834,134 L834,181 L0,181 Z" fill="var(--orange)"/>
  </svg>
  <p class="cta">RSVP online at stridereformstudio.com</p>
</main>
</body>
</html>
```